www.vandrik.com Sales/Order Page ReDesign

We need a new and amazing design for our sales/order page to attract more costumers and new houses for our portal.

Here is the existing page with the current design: https://www.vandrik.com/sales

We are proud owners of www.hyttetun.no and www.vandrik.com and we want more holiday home owners to join our page so that we can rent out their holiday homes and increase the number of houses on our portal.

To get more homeowners we need a sales page that can sell our products the best way possible. Therefore we want you too blow us away with a fresh, modern, easy understandable and stylish new sales/order page.

The only restrictions we give when it comes to design is that it needs to fit the existing design of our portals, the top and footer are set. Beside that we are open for everything as long as it at once give the customers impression that this is a good, professional page were they just have to put out their houses.

When it comes to content I have added two documents who include the content to put in here and some guidelines on how to organize the page. Please be creative and add necessary graphics, symbols, background pictures and what ever necessary to make this page look professional and appealing to new costumers.

Looking forward to what suggestions we are given.
Updates

We just want to inform that we have updated our brief with a much more concrete description of what content to add on the sale page, and who to structure the content on the page. Hope this helps to make suggestions easier. Looking forward to receive some good contributions.

We would just like to make sure that everyone have understood that we are not asking for a new design suggestion to our portal in general. We are only asking for a redesign of our sales/order page you find here www.vandrik.com/sales. We have to day received some designs for our front page and the design it self was good, but that's not what we are asking for this time and don't want you to use time of something we don't need at the moment. We are looking forward too se some good suggestions.

Project Deadline Extended
Reason: Hello. Thanks for all the great contributions we have been given so fare. We haven't been able to respond to all design and are therefore extending the deadline so that we are able to respond to the designs we have been giver and to gov time to make final changes.

Project Deadline Extended
Reason: We are extending the deadline to give designers time to give new suggestion based on our latest feedback today.

Project Deadline Extended
Reason: Extended so we can receive last design changes.

Target Market(s)

This is a presentation page where we present our product agains new home owner who we what to choose listing there property on or site.

Industry/Entity Type

Sales

Requirements
Must have
• A modern design who calms the costumer down and help them in deciding to chose us, and for them to choose us they need to trust and believe in us. Therefore your main task is to create a page that effectively informs about our product, gets the visitors attentions and make them trust us.
Nice to have
• Examples of good competitors and good order pages we like:

http://www.stayplume.com/info/lyp?icid=IL___O_Text___top_nav_link
https://www.nestorly.com/rooms/new
https://www.quince.com/tablo/compare/
http://www.lodgewick.com/host
Should not have
• - Bad design :-). With bad design we mean design that looks like it's made in 2 seconds by a little child.

```html
<!DOCTYPE html>
<html lang="en">
<head>
<meta charset="utf-8">
<title>List your property – Sales</title>
<link rel="stylesheet" href="https://fonts.googleapis.com/css2?family=Raleway:wght@300;400;500;600&display=swap">
<style>
  :root {
    --page-bg: #ffffff;
    --section-bg: #fafafa;
    --green-tint: #f3f9e6;
    --peach-tint: #fcf1ec;
    --grey-band: #f3f3f3;
    --green: #86d100;
    --orange: #ff6d00;
    --blue: #0084d1;
    --text: #111111;
    --muted: #d0d0d0;
    --addon-bg: #efefef;
  }
  * { box-sizing: border-box; margin: 0; padding: 0; }
  html, body { width: 1200px; height: 953px; overflow: hidden; }
  body { background: var(--page-bg); font-family: "Raleway", sans-serif; color: var(--text); position: relative; }
  .abs { position: absolute; }
  .sheet { left: 100px; top: 0; width: 1000px; height: 953px; background: var(--section-bg); }

  .panel { top: 0; height: 200px; width: 480px; }
  .panel--list { left: 120px; background: var(--green-tint); }
  .panel--contact { left: 600px; background: var(--peach-tint); }
  .panel p { position: absolute; top: 25px; font-size: 14px; line-height: 24px; }
  .panel--list p { left: 22px; width: 430px; }
  .panel--contact p { left: 12px; width: 440px; }

  .pill { display: flex; align-items: center; justify-content: center; height: 50px; width: 450px; border-radius: 25px; color: #fff; font-size: 14px; font-weight: 500; text-decoration: none; }
  .pill--green { background: var(--green); }
  .pill--orange { background: var(--orange); }

  .hint-band { left: 100px; top: 225px; width: 1000px; height: 50px; background: var(--green-tint); font-size: 12px; padding: 15px 0 0 35px; font-weight: 500; }
  .hint-band a { color: var(--blue); }

  .calc-title { left: 137px; top: 303px; font-size: 31px; font-weight: 400; }
  .calc-close { left: 1033px; top: 310px; }
  .calc-intro { left: 140px; top: 360px; width: 920px; font-size: 12px; line-height: 18px; }

  .label { font-size: 14px; font-weight: 500; }
  .toggle { display: flex; align-items: center; justify-content: center; height: 52px; font-size: 14px; font-weight: 500; border: 1px solid var(--blue); }
  .toggle--on { background: var(--blue); color: #fff; }
  .toggle--off { background: #fff; }
  .field { display: flex; height: 52px; border: 1px solid var(--blue); background: #fff; }
  .field .addon { background: var(--addon-bg); display: flex; align-items: center; justify-content: center; font-size: 14px; font-weight: 500; }
  .field .addon--left { border-right: 1px solid var(--blue); color: #777; }
  .field .addon--right { border-left: 1px solid var(--blue); }

  .price { text-align: right; width: 160px; left: 900px; }
  .price .cur { color: var(--muted); font-size: 40px; font-weight: 300; vertical-align: 4px; margin-right: 6px; }
  .price .amt { color: var(--blue); font-size: 58px; font-weight: 300; }
  .per { font-size: 19px; width: 100px; text-align: right; left: 960px; }
  .vs { left: 722px; top: 488px; font-size: 25px; color: var(--muted); font-weight: 300; }

  .callback { left: 100px; top: 651px; width: 1000px; height: 184px; background: var(--peach-tint); }
  .callback p { position: absolute; left: 53px; top: 25px; width: 910px; font-size: 14px; line-height: 24px; }

  .detail-band { left: 100px; top: 835px; width: 1000px; height: 68px; background: var(--grey-band); }
  .detail-band h2 { position: absolute; left: 35px; top: 19px; font-size: 25px; font-weight: 500; }
</style>
</head>
<body>
  <div class="abs sheet"></div>

  <section class="abs panel panel--list">
    <p>You have not chosen to list any property with us, add a property by clicking Add New Property below</p>
  </section>
  <section class="abs panel panel--contact">
    <p>If you want us to contact you too answer any question Contact Us button</p>
  </section>
  <a class="abs pill pill--green" style="left:141px;top:100px;">Add New Property</a>
  <a class="abs pill pill--orange" style="left:611px;top:100px;">Contact Us</a>

  <div class="abs hint-band">You now know that you are going to list your property, but are uncertain which listing option is right for you? <a>Click here</a> to calculate what’s most profitable for you..</div>

  <h1 class="abs calc-title">Which listing option should you choose?</h1>
  <svg class="abs calc-close" width="32" height="32" viewBox="0 0 32 32" aria-label="Close">
    <path d="M2 2 L30 30 M30 2 L2 30" stroke="#bbb" stroke-width="1.5" fill="none"/>
  </svg>
  <p class="abs calc-intro">As a general rule, pay-per-booking is a better value than an annual subscription for properties that are rented less than six weeks a year. But don't take our word for it! Enter your rates below to see which option is best for you.</p>

  <span class="abs label" style="left:138px;top:450px;">Rate</span>
  <div class="abs toggle toggle--on" style="left:205px;top:433px;width:78px;">Daily</div>
  <div class="abs toggle toggle--off" style="left:293px;top:433px;width:83px;">Weekly</div>
  <div class="abs field" style="left:385px;top:433px;width:215px;">
    <span class="addon addon--left" style="width:46px;">€</span>
    <span style="flex:1;"></span>
    <span class="addon addon--right" style="width:59px;">/day</span>
  </div>

  <span class="abs label" style="left:243px;top:545px;">Average Annual Bookings</span>
  <div class="abs field" style="left:430px;top:528px;width:170px;">
    <span style="flex:1;"></span>
    <span class="addon addon--right" style="width:59px;">days</span>
  </div>

  <span class="abs label" style="left:638px;top:450px;">Estimated pay-per-booking cost</span>
  <div class="abs price" style="top:420px;"><span class="cur">€</span><span class="amt">40</span></div>
  <span class="abs per" style="top:482px;">/year</span>

  <span class="abs vs">vs</span>

  <span class="abs label" style="left:638px;top:545px;">Cost of a Classic subscription</span>
  <div class="abs price" style="top:515px;"><span class="cur">€</span><span class="amt">349</span></div>
  <span class="abs per" style="top:579px;">/year</span>

  <section class="abs callback">
    <p>If you want personal guidelines we are more then willing to call you, type in your name and number here and someone will contact you as soon as possible</p>
  </section>
  <a class="abs pill pill--orange" style="left:152px;top:750px;">Contact Us</a>

  <section class="abs detail-band"><h2>Customer Detail</h2></section>
</body>
</html>
```